Company Presentation re-design.

We need to create a new 15-20 pager-presentation that will show KORVALE (travel management company) as a client-centric company with a human-to-human approach. As a start we ask a Designers to create a 3 page test presentation so we can choose the winner. who will then design the rest slides

Two main idears are to be shown on the slides:
• KORVALE is client-centric company who believes in partnership with corporate clients;
• KORVALE is a stable and trustworthy partner;

The test slides should be:

Slide (1) - Our strategy is Customer – centric strategy. KORVALE bases its business approach on the customer needs. 5 qualities that identify KORVALE as a customer-centric :
1. corporate culture, aimed at customers' changing needs
2. professional Key Account Manager (KAM)
3. Each product solution meets specific client needs.
4. innovation
5. security policy

Slide (2) - Our product solutions of clients needs
The main idea of this page is to describe our products for customers. KORVALE has 5 main products:
1. Business Travel
2. Service
3. On-line booking
4. MICE & Congress
5. Non-standard services

Slide (3)
This page shows the highlights of KORVALE support and it is shown in a cloud design now.

Attched pls find our current presentation

Dear Professionals! Please pay attantion that we updated the project by doubled the budjet! Wait for yiour grate ideas. 

Target Market(s)

Mid to top management (practically any industry), travel coordinators, procurement specialists, corporate buyers etc, travelers

Industry/Entity Type

Security

Requirements
Must have
• (1) The presentation must visualize the text above, with as little text itself as possible.
(2) We would appreciate ideas with INFOGRAPHIC
(3) Design of the presentation is up to the company logo in all variations. ( attached files).
(4) We would like to see designs that use grey, blue, orange and maroon colors - corporate colors of our logo.
Nice to have
• Infografics
Designs we like:
to brintaly.com+; zumoth.com; pelvanstudio.com; tarnowatt.co.uk (infografics)

```html
<!DOCTYPE html>
<html lang="ru">
<head>
<meta charset="utf-8">
<title>KORVALE — Наши продуктовые решения для вас</title>
<link rel="stylesheet" href="https://fonts.googleapis.com/css2?family=Yanone+Kaffeesatz:wght@300;400&display=swap">
<style>
  :root {
    --bg-center: #f4f4f4;
    --bg-edge: #d9dadb;
    --banner: #3b3e41;
    --banner-fold: #1f2123;
    --text: #2e3033;
    --blue: #4a7db3;
    --rule: #8fa0b0;
    --footer: #8b8d8f;
    --footer-text: #ffffff;
    --city-light: #e6e8eb;
    --city-mid: #c9ccd0;
    --city-blue: #b9c8d9;
  }
  * { margin: 0; padding: 0; box-sizing: border-box; }
  html, body { width: 1200px; height: 831px; overflow: hidden; }
  body { font-family: "Yanone Kaffeesatz", "Arial Narrow", sans-serif; color: var(--text); }

  .slide {
    position: relative; width: 1200px; height: 831px; overflow: hidden;
    background: radial-gradient(ellipse at 50% 45%, var(--bg-center) 0%, #ebebec 55%, var(--bg-edge) 100%);
  }

  .title-banner {
    position: absolute; left: 65px; top: 43px; width: 555px; height: 65px;
    background: var(--banner); color: #fff;
    font-weight: 300; font-size: 35px; letter-spacing: 1px; text-transform: uppercase;
    display: flex; align-items: center; padding-left: 34px;
  }
  .title-fold {
    position: absolute; left: 600px; top: 108px; width: 0; height: 0;
    border-left: 20px solid transparent; border-top: 14px solid var(--banner-fold);
  }

  .city-compass {
    position: absolute; left: 290px; top: 140px; width: 620px; height: 570px;
    border-radius: 50%;
    background: radial-gradient(circle at 50% 50%, #ffffff 0%, #ffffff 24%, var(--city-mid) 25%, #a9adb2 34%, var(--city-light) 36%, var(--city-mid) 52%, var(--city-blue) 64%, rgba(220,223,227,0) 72%);
    opacity: .9;
  }

  .graphics { position: absolute; inset: 0; }

  .point { position: absolute; display: flex; align-items: flex-start; }
  .point-num {
    font-weight: 300; font-size: 32px; line-height: 1; color: var(--blue);
    padding-right: 6px; margin-top: -1px;
  }
  .point-text {
    border-left: 1px solid var(--rule); padding-left: 7px;
    font-weight: 300; font-size: 19px; line-height: 23px; text-transform: uppercase;
    letter-spacing: .3px;
  }
  .p1 { left: 152px; top: 215px; }
  .p2 { left: 887px; top: 219px; }
  .p3 { left: 887px; top: 452px; }
  .p4 { left: 887px; top: 650px; }
  .p5 { left: 145px; top: 633px; }

  .footer {
    position: absolute; left: 0; bottom: 0; width: 1200px; height: 56px;
    background: var(--footer); color: var(--footer-text);
    display: flex; align-items: center;
  }
  .brand { position: absolute; left: 66px; top: 10px; font-weight: 400; font-size: 32px; letter-spacing: 1px; }
  .motto { position: absolute; left: 0; width: 1175px; text-align: center; font-weight: 300; font-size: 19px; }
  .site { position: absolute; right: 62px; font-weight: 300; font-size: 19px; }
</style>
</head>
<body>
<main class="slide">
  <h1 class="title-banner">Наши продуктовые решения для вас</h1>
  <div class="title-fold"></div>

  <div class="city-compass" role="img" aria-label="Круговой силуэт городов мира вокруг компаса"></div>

  <svg class="graphics" width="1200" height="831" viewBox="0 0 1200 831" aria-hidden="true">
    <defs>
      <symbol id="plane" viewBox="0 0 60 80">
        <path fill="#4a7db3" d="M30 2C33 2 34 8 34 14L34 30L58 44L58 50L34 42L34 62L42 69L42 74L30 70L18 74L18 69L26 62L26 42L2 50L2 44L26 30L26 14C26 8 27 2 30 2Z"/>
      </symbol>
    </defs>

    <!-- route 01 -->
    <path d="M103 240 C105 270 125 289 155 290 L338 290" fill="none" stroke="#4a7db3" stroke-width="1.5" stroke-dasharray="1.5 3"/>
    <use href="#plane" x="75" y="155" width="60" height="80"/>

    <!-- route 02 -->
    <path d="M1130 195 L910 195 C880 195 868 215 868 240 C868 270 885 293 915 293 L1200 293" fill="none" stroke="#4a7db3" stroke-width="1.5" stroke-dasharray="1.5 3"/>
    <use href="#plane" x="0" y="0" width="60" height="80" transform="translate(1125 225) rotate(-90)"/>
    <use href="#plane" x="0" y="0" width="36" height="48" transform="translate(872 306) rotate(-70)"/>

    <!-- route 04 -->
    <path d="M1150 395 L1150 775" fill="none" stroke="#4a7db3" stroke-width="1.3" stroke-dasharray="6 3 1.5 3"/>
    <path d="M1150 738 L655 738" fill="none" stroke="#4a7db3" stroke-width="1.3" stroke-dasharray="4 3"/>
    <use href="#plane" x="1116" y="310" width="68" height="90"/>
    <use href="#plane" x="0" y="0" width="68" height="90" transform="translate(565 772) rotate(-90)"/>

    <!-- route 05 -->
    <path d="M178 612 L178 585" fill="none" stroke="#4a7db3" stroke-width="1.5" stroke-dasharray="1.5 3"/>
    <use href="#plane" x="145" y="492" width="66" height="86"/>
  </svg>

  <section class="point p1"><span class="point-num">01</span><p class="point-text">Корпоративная культура<br>нацелена на меняющиеся<br>потребности клиентов</p></section>
  <section class="point p2"><span class="point-num">02</span><p class="point-text">Точка доступа к<br>интеллектуальной<br>экспертизе компании – КАМ</p></section>
  <section class="point p3"><span class="point-num">03</span><p class="point-text">Каждое продуктовое<br>решение отвечает<br>конкретным задачам клиента</p></section>
  <section class="point p4"><span class="point-num">04</span><p class="point-text">Внедрение новых решений<br>и постоянные инновации</p></section>
  <section class="point p5"><span class="point-num">05</span><p class="point-text">Забота о безопасности<br>путешественника и<br>персональных данных</p></section>

  <footer class="footer">
    <span class="brand">KORVALE</span>
    <span class="motto">Always learning – always growing</span>
    <span class="site">www.korvale.ru</span>
  </footer>
</main>
</body>
</html>
```